Business Card Design Project

We require a professional business card designed for our consulting organisation that has the same theme and colours as our logo except for the grey.

Colours on the front should predominately be white however some reference to our logo colours except for the grey.

The back of the card should be have background colour that aligns with our logo colour.

Layout, style and design is up to the designer. So send through your designs

Details are attached in the word document project brief.

Target Market(s)

Target market are large corporate organisations

Industry/Entity Type

Business

Requirements
Must have
• Content on the front must have:

Dale Fenwick
Managing Director

P: 0412 557 208
E: Dale@braviotraxgroup.com
W: www.braviotraxgroup.com

Content on the back must have the words:
Alliances
Placement
Training
Support

Design Colours
Must align to our logo

```html
<!DOCTYPE html>
<html lang="en">
<head>
<meta charset="utf-8">
<title>Business Card Design: 05</title>
<link href="https://fonts.googleapis.com/css2?family=Open+Sans:wght@400;600;700&family=Source+Serif+4:wght@400&display=swap" rel="stylesheet">
<style>
  :root {
    --canvas: #ffffff;
    --ink: #1a1a1a;
    --brand-blue: #1b75bb;
    --card-blue: #1592d3;
    --card-edge: #cfcfcf;
    --tile-ink: #0d0d0d;
    --white: #ffffff;
  }
  * { margin: 0; padding: 0; box-sizing: border-box; }
  html, body {
    width: 1200px; height: 900px; overflow: hidden;
    background: var(--canvas);
  }
  .sheet { position: relative; width: 1200px; height: 900px; }

  .sheet-title, .view-caption {
    position: absolute;
    font-family: "Source Serif 4", Georgia, serif;
    font-size: 17px; font-weight: 400; color: var(--ink);
    text-align: center;
  }
  .sheet-title { left: 0; width: 1200px; top: 261px; }
  .view-caption { top: 619px; width: 510px; }
  .view-caption.front { left: 76px; }
  .view-caption.back { left: 614px; }

  .card {
    position: absolute; top: 320px; width: 511px; height: 288px;
    font-family: "Open Sans", Arial, sans-serif;
    box-shadow: 4px 5px 7px rgba(0,0,0,0.28);
    overflow: hidden;
  }
  .card-front { left: 76px; background: var(--white); border: 1px solid var(--card-edge); }
  .card-back { left: 614px; background: var(--card-blue); }

  .holder-name { position: absolute; left: 28px; top: 24px; font-size: 22px; color: var(--ink); }
  .holder-role { position: absolute; left: 29px; top: 54px; font-size: 11px; color: var(--ink); }
  .contact { position: absolute; left: 29px; color: var(--ink); }
  .contact .value { font-size: 12px; display: block; }
  .contact .label { font-size: 9px; letter-spacing: 0.4px; display: block; margin-top: 1px; }
  .contact.phone { top: 102px; }
  .contact.email { top: 141px; }
  .website { position: absolute; left: 29px; top: 245px; font-size: 12px; color: var(--brand-blue); }

  .brand {
    position: absolute; display: flex; align-items: center; gap: 12px;
    font-weight: 700; font-size: 22px; line-height: 1.05;
  }
  .brand .mark { width: 34px; height: 34px; flex: none; }
  .brand .word { display: block; white-space: nowrap; }
  .card-front .brand { left: 270px; top: 110px; color: var(--brand-blue); }
  .card-front .brand .mark { background: var(--brand-blue); }
  .card-back .brand { left: 42px; top: 120px; color: var(--white); }
  .card-back .brand .mark { background: var(--white); }

  .service-tile {
    position: absolute; width: 92px; height: 91px;
    border: 3px solid var(--tile-ink); border-radius: 13px;
  }
  .service-tile .icon {
    position: absolute; left: 24px; top: 10px; width: 38px; height: 38px;
    background: var(--tile-ink); border-radius: 6px; opacity: 0.9;
  }
  .service-tile .name {
    position: absolute; left: 0; right: 0; top: 66px;
    text-align: center; font-size: 9px; font-weight: 700;
    letter-spacing: 0.5px; color: var(--tile-ink);
  }
  .tile-alliances { left: 279px; top: 49px; }
  .tile-placements { left: 379px; top: 49px; }
  .tile-training { left: 279px; top: 148px; }
  .tile-support { left: 379px; top: 148px; }
</style>
</head>
<body>
<main class="sheet">
  <h1 class="sheet-title">Business Card Design: 05</h1>

  <section class="card card-front">
    <p class="holder-name">Dale Fenwick</p>
    <p class="holder-role">Managing Director</p>
    <p class="contact phone"><span class="value">0412 557 208</span><span class="label">PHONE</span></p>
    <p class="contact email"><span class="value">Dale@braviotraxgroup.com</span><span class="label">EMAIL</span></p>
    <p class="website">www.braviotraxgroup.com</p>
    <div class="brand"><span class="mark"></span><span><span class="word">Braviotrax</span><span class="word">Group</span></span></div>
  </section>

  <section class="card card-back">
    <div class="brand"><span class="mark"></span><span><span class="word">Braviotrax</span><span class="word">Group</span></span></div>
    <div class="service-tile tile-alliances">
      <span class="icon" role="img" aria-label="Handshake icon"></span>
      <span class="name">ALLIANCES</span>
    </div>
    <div class="service-tile tile-placements">
      <span class="icon" role="img" aria-label="Puzzle pieces icon"></span>
      <span class="name">PLACEMENTS</span>
    </div>
    <div class="service-tile tile-training">
      <span class="icon" role="img" aria-label="Trainer at a board icon"></span>
      <span class="name">TRAINING</span>
    </div>
    <div class="service-tile tile-support">
      <span class="icon" role="img" aria-label="Support person icon"></span>
      <span class="name">SUPPORT</span>
    </div>
  </section>

  <p class="view-caption front">Front Side View</p>
  <p class="view-caption back">Back Side View</p>
</main>
</body>
</html>
```